Website design for Tallow Ridge Trading Inc

We are looking to build a website for our company. We are a scrap metal recycling company based out of Los Angeles. We purchase scrap metal in the US and ship them to China for recycling into fresh metal ores to supply industrial users. We would designs that emphasize the color green given our name and the nature of our business. Recycling themes are welcomed. We already have a URL at:
http://tallowridgetradinginc.example/
At this point, I would like 4 pages:
- Home page
- About Us
- Resources
- Contact us
Our sister company is Marrow Peak Intl Inc and they have a website that we can use as a starting point.
http://www.marrowpeak-intl.example/
Our competitor has a website below. However we dislike the design given we believe it looks rather dull.
http://www.vesperalloyworks.example/en/
Lastly, this is for a website shell only. Please design the template, graphics, and color schemes. We will write the contents later.

```html
<!DOCTYPE html>
<html lang="en">
<head>
<meta charset="utf-8">
<title>Tallow Ridge Trading, Inc</title>
<link rel="stylesheet" href="https://fonts.googleapis.com/css2?family=Open+Sans:wght@400;600;700&family=Arimo:wght@400;700&display=swap">
<style>
:root{
  --green:#4fa516;
  --footer-green:#639f00;
  --footer-text:#fdf8d8;
  --ink:#333333;
  --body-ink:#2b2b2b;
  --nav-ink:#3a3a3a;
  --icon-grey:#8a8a8a;
  --tick-red:#d10000;
  --rule:#c9c9c9;
  --frame:#ffffff;
}
*{margin:0;padding:0;box-sizing:border-box}
html,body{width:1200px;height:1000px;overflow:hidden}
body{
  position:relative;
  font-family:"Open Sans",Arial,sans-serif;
  color:var(--ink);
  background:linear-gradient(180deg,#e4e4e4 0,#f2f2f2 140px,#ffffff 420px,#f7f7f7 600px,#e9e9e9 780px,#d9d9d9 858px);
}
.page-top{position:absolute;left:0;top:0;width:1200px;height:10px;background:linear-gradient(#cfcfcf,#eeeeee)}
.header-sweep{position:absolute;left:0;top:0}
.brand{position:absolute;left:175px;top:40px;display:flex;align-items:center;gap:14px}
.brand-mark{width:56px;height:56px;background:var(--green)}
.brand-name{font-weight:700;font-size:26px;line-height:28px;color:var(--green);width:260px;letter-spacing:.3px}
.main-nav{position:absolute;top:60px;left:640px;display:flex;gap:26px}
.main-nav a{display:flex;align-items:center;gap:8px;font-size:13.5px;font-weight:600;color:var(--nav-ink);text-decoration:none;letter-spacing:.2px}
.nav-icon{width:14px;height:14px}
.showcase{position:absolute;left:0;top:170px}
.welcome{position:absolute;left:147px;top:458px;width:960px}
.welcome h1{font-size:20.5px;font-weight:700;color:var(--green);margin-bottom:4px}
.welcome p{font-size:13px;line-height:22px;text-align:justify;color:var(--body-ink)}
.divider{position:absolute;left:147px;top:595px;width:960px;height:5px;border-top:1px solid var(--rule);border-bottom:1px solid var(--rule)}
.why-us{position:absolute;left:158px;top:615px;width:620px}
.why-us h2,.highlights h2{font-size:16.5px;font-weight:700;color:var(--ink);margin-bottom:2px}
.why-us p{font-family:Arimo,Arial,sans-serif;font-size:12.6px;line-height:21px;text-align:justify;color:var(--body-ink)}
.highlights{position:absolute;left:819px;top:615px;width:290px}
.highlights h2{margin-bottom:8px}
.highlights ul{list-style:none}
.highlights li{display:flex;align-items:center;gap:8px;height:30px;font-family:Arimo,Arial,sans-serif;font-size:12.6px;color:var(--body-ink)}
.tick{width:17px;height:17px;flex:none}
.site-footer{position:absolute;left:0;top:860px;width:1200px;height:140px;border-top:4px solid #ffffff;background:var(--footer-green)}
.footer-nav{position:absolute;left:147px;top:18px;display:flex;gap:21px;font-size:13px;font-weight:700;color:var(--footer-text)}
.footer-nav a{color:var(--footer-text);text-decoration:none}
.copyright{position:absolute;left:147px;top:44px;font-size:12.5px;color:var(--footer-text)}
.social{position:absolute;left:1043px;top:21px;display:flex;gap:8px}
.social span{width:27px;height:27px;border-radius:4px;background:#dfe8cf;display:block}
</style>
</head>
<body>
<div class="page-top"></div>
<svg class="header-sweep" width="1200" height="440" viewBox="0 0 1200 440" aria-hidden="true">
  <defs>
    <linearGradient id="sweepFill" x1="0" y1="0" x2="0" y2="1">
      <stop offset="0" stop-color="#e6e6e6"/>
      <stop offset="1" stop-color="#f6f6f6"/>
    </linearGradient>
  </defs>
  <path d="M0 10 H1200 V110 Q600 230 0 110 Z" fill="url(#sweepFill)"/>
  <path d="M0 110 Q600 230 1200 110" fill="none" stroke="#ffffff" stroke-width="3" opacity=".9"/>
  <path d="M0 120 L150 205" stroke="#ffffff" stroke-width="2" opacity=".7"/>
  <path d="M1200 110 L1040 205" stroke="#ffffff" stroke-width="2" opacity=".7"/>
</svg>

<header>
  <a class="brand" href="http://tallowridgetradinginc.example/">
    <span class="brand-mark"></span>
    <span class="brand-name">Tallow Ridge Trading, Inc</span>
  </a>
  <nav class="main-nav">
    <a href="#"><svg class="nav-icon" viewBox="0 0 14 14"><circle cx="7" cy="7" r="7" fill="#8a8a8a"/><path d="M4 7h5M7 4.5L9.5 7 7 9.5" stroke="#fff" stroke-width="1.6" fill="none"/></svg>HOME</a>
    <a href="#"><svg class="nav-icon" viewBox="0 0 14 14"><circle cx="7" cy="7" r="7" fill="#8a8a8a"/><path d="M4 7h5M7 4.5L9.5 7 7 9.5" stroke="#fff" stroke-width="1.6" fill="none"/></svg>ABOUT US</a>
    <a href="#"><svg class="nav-icon" viewBox="0 0 14 14"><circle cx="7" cy="7" r="7" fill="#8a8a8a"/><path d="M4 7h5M7 4.5L9.5 7 7 9.5" stroke="#fff" stroke-width="1.6" fill="none"/></svg>RESOURCES</a>
    <a href="#"><svg class="nav-icon" viewBox="0 0 14 14"><circle cx="7" cy="7" r="7" fill="#8a8a8a"/><path d="M4 7h5M7 4.5L9.5 7 7 9.5" stroke="#fff" stroke-width="1.6" fill="none"/></svg>CONTATC US</a>
  </nav>
</header>

<svg class="showcase" width="1200" height="260" viewBox="0 170 1200 260">
  <defs>
    <linearGradient id="scrapGrey" x1="0" y1="0" x2="1" y2="1">
      <stop offset="0" stop-color="#9a9a9a"/><stop offset=".5" stop-color="#d4d4d4"/><stop offset="1" stop-color="#5e5e5e"/>
    </linearGradient>
    <linearGradient id="scrapSky" x1="0" y1="0" x2="0" y2="1">
      <stop offset="0" stop-color="#3f8fd6"/><stop offset=".45" stop-color="#8fc2ea"/><stop offset=".6" stop-color="#6c6c6c"/><stop offset="1" stop-color="#2a2a2a"/>
    </linearGradient>
    <linearGradient id="scrapBlue" x1="0" y1="0" x2="1" y2="1">
      <stop offset="0" stop-color="#5a6e86"/><stop offset=".5" stop-color="#b5c3d4"/><stop offset="1" stop-color="#7a7064"/>
    </linearGradient>
    <linearGradient id="reflect" x1="0" y1="0" x2="0" y2="1">
      <stop offset="0" stop-color="#d8d8d8"/><stop offset="1" stop-color="#ffffff" stop-opacity="0"/>
    </linearGradient>
  </defs>
  <polygon points="144,205 356,234 356,345 144,365" fill="var(--frame)"/>
  <polygon points="147,210 352,238 352,340 147,360" fill="url(#scrapGrey)" role="img" aria-label="Pile of shredded scrap metal"/>
  <polygon points="144,368 356,348 356,390 144,395" fill="url(#reflect)"/>
  <polygon points="1110,205 898,234 898,345 1110,365" fill="var(--frame)"/>
  <polygon points="902,238 1107,212 1107,360 902,340" fill="url(#scrapBlue)" role="img" aria-label="Metal turnings and shavings"/>
  <polygon points="898,348 1110,368 1110,395 898,390" fill="url(#reflect)"/>
  <rect x="366" y="181" width="522" height="210" fill="var(--frame)"/>
  <rect x="371" y="186" width="512" height="200" fill="url(#scrapSky)" role="img" aria-label="Crane lifting crushed cars over a scrap yard"/>
  <rect x="371" y="396" width="512" height="28" fill="url(#reflect)"/>
</svg>

<section class="welcome">
  <h1>Welcome to Tallow Ridge Trading, Inc.</h1>
  <p>Cras ultricies ligula et massa faucibus condimentum. Cras venenatis quam ullamcorper nisi hendrerit ultricies. Integer pulvinar mollis massa, et tincidunt augue pulvinar id. Aenean vitae aliquam velit, in tristique erat. Pellentesque habitant morbi tristique senectus et netus et malesuada fames ac turpis egestas. Donec laoreet lorem in odio volutpat interdum. Cras cursus turpis dui, id fringilla sapien mollis vitae.</p>
</section>

<div class="divider"></div>

<section class="why-us">
  <h2>Why Us?</h2>
  <p>Cras ultricies ligula et massa faucibus condimentum. Cras venenatis quam ullamcorper nisi hendrerit ultricies. Integer pulvinar mollis massa, et tincidunt augue pulvinar id. Aenean vitae aliquam velit, in tristique erat. Pellentesque habitant morbi tristique senectus et netus et malesuada fames ac turpis egestas. Donec laoreet lorem in odio volutpat interdum. Cras cursus turpis dui, id fringilla sapien mollis vitae. Vivamus vehicula dui nec tellus porta, vel sagittis enim tristique.</p>
</section>

<section class="highlights">
  <h2>Pellentesque dignissim:</h2>
  <ul>
    <li><svg class="tick" viewBox="0 0 17 17"><path d="M1 9 L6 15 L16 1" fill="none" stroke="#d10000" stroke-width="2.6"/></svg>Ut bibendum lorem sed mollis sodales.</li>
    <li><svg class="tick" viewBox="0 0 17 17"><path d="M1 9 L6 15 L16 1" fill="none" stroke="#d10000" stroke-width="2.6"/></svg>Donec vitae massa blandit</li>
    <li><svg class="tick" viewBox="0 0 17 17"><path d="M1 9 L6 15 L16 1" fill="none" stroke="#d10000" stroke-width="2.6"/></svg>Pellentesque egestas cursus dictum.</li>
    <li><svg class="tick" viewBox="0 0 17 17"><path d="M1 9 L6 15 L16 1" fill="none" stroke="#d10000" stroke-width="2.6"/></svg>Aliquam vulputate lo</li>
  </ul>
</section>

<footer class="site-footer">
  <nav class="footer-nav">
    <a href="#">Home</a><span>|</span>
    <a href="#">About Us</a><span>|</span>
    <a href="#">Resources</a><span>|</span>
    <a href="#">Contact Us</a>
  </nav>
  <p class="copyright">Copyright © 2013 Tallow Ridge Trading, Inc. All rights reserved.</p>
  <div class="social"><span></span><span></span></div>
</footer>
</body>
</html>
```